Harborline Crest Insurance Services

we are a high end insurance agency we specialize on Auto | Home | Business | Life looking for something professional and luxuries at the same time. if you guys need anything else please let me know.

Auto | Home | Business | Life must be under logo on the back with black background.

i want the back part to be black with our gold logo on it.

Target Market(s)

Auto | Home | Business | Life

Industry/Entity Type

Insurance Broker

Contact Information for Business Card

My logo is gold so a black in the back would be nice.

Font styles to use
Serif

Colors
000000

Requirements
Must have
• Big logo on the back with black background.

```html
<!DOCTYPE html>
<html lang="en">
<head>
<meta charset="utf-8">
<title>Harborline Crest Insurance Services — Business Card</title>
<link rel="stylesheet" href="https://fonts.googleapis.com/css2?family=Cinzel:wght@600&family=Lato:wght@400;700&display=swap">
<style>
  :root {
    --backdrop: #6d6058;
    --card-black: #000000;
    --card-white: #ffffff;
    --gold: #f2bb1a;
    --gold-line: #f0c64a;
    --ink: #2b2b2b;
    --rule-grey: #cfcfcf;
    --serif: "Cinzel", Georgia, serif;
  }
  * { margin: 0; padding: 0; box-sizing: border-box; }
  html, body { width: 1200px; height: 960px; overflow: hidden; }
  body {
    background: var(--backdrop);
    position: relative;
    font-family: "Lato", Arial, sans-serif;
  }
  .card {
    position: absolute;
    width: 662px;
    height: 380px;
    overflow: hidden;
  }
  .card--front { left: 273px; top: 73px; background: var(--card-black); }
  .card--back  { left: 272px; top: 508px; background: var(--card-white); }

  .brand {
    position: absolute;
    display: flex;
    flex-direction: column;
    align-items: center;
    color: var(--gold);
    font-family: var(--serif);
    font-weight: 600;
    text-align: center;
    white-space: nowrap;
  }
  .brand__dot {
    width: 110px; height: 110px;
    border-radius: 50%;
    background: var(--gold);
    margin-bottom: 20px;
  }
  .brand__name { font-size: 34px; line-height: 1; }
  .brand__tag  { font-size: 15px; line-height: 1; letter-spacing: 4px; margin-top: 11px; text-transform: uppercase; }
  .card--front .brand { left: 0; width: 662px; top: 68px; }

  .back-panel { position: absolute; inset: 0; }
  .card--back .brand { left: 340px; width: 310px; top: 82px; }
  .card--back .brand__dot { width: 100px; height: 100px; margin-bottom: 16px; }
  .card--back .brand__name { font-size: 26px; }
  .card--back .brand__tag { font-size: 12px; letter-spacing: 3px; margin-top: 9px; }
  .brand__lines { font-size: 12px; line-height: 1; letter-spacing: 1.5px; margin-top: 12px; }

  .contact { position: absolute; left: 31px; top: 82px; color: var(--ink); }
  .contact__name {
    color: var(--gold);
    font-size: 20px;
    font-weight: 700;
    letter-spacing: 2px;
    text-transform: uppercase;
    line-height: 24px;
  }
  .contact__role { font-size: 16px; letter-spacing: 1.5px; line-height: 20px; }
  .rule { width: 176px; height: 1px; background: var(--gold-line); margin: 11px 0 11px; }
  .rule--grey { background: var(--rule-grey); margin: 6px 0 15px; }
  .contact__address { font-size: 16px; line-height: 20px; letter-spacing: 0.8px; }
  .contact__list { list-style: none; font-size: 15.5px; line-height: 21.5px; letter-spacing: 0.4px; }
  .contact__list li { display: flex; align-items: center; gap: 6px; }
  .icon { width: 13px; height: 13px; flex: none; fill: var(--gold); }
</style>
</head>
<body>

<section class="card card--front" aria-label="Card front">
  <div class="brand">
    <span class="brand__dot"></span>
    <span class="brand__name">Harborline Crest</span>
    <span class="brand__tag">Insurance Services</span>
  </div>
</section>

<section class="card card--back" aria-label="Card back">
  <svg class="back-panel" width="662" height="380" viewBox="0 0 662 380">
    <defs>
      <linearGradient id="edge-sheen" x1="0" y1="0" x2="0" y2="1">
        <stop offset="0" stop-color="#e6e6e6"/>
        <stop offset="0.6" stop-color="#8a8a8a"/>
        <stop offset="1" stop-color="#3a3a3a"/>
      </linearGradient>
    </defs>
    <path d="M398,0 C330,90 300,250 378,380 L662,380 L662,0 Z" fill="var(--card-black)"/>
    <path d="M392,0 C330,80 306,200 324,290" fill="none" stroke="url(#edge-sheen)" stroke-width="7" stroke-linecap="round"/>
  </svg>

  <div class="contact">
    <p class="contact__name">Marisol Whitaker</p>
    <p class="contact__role">Director</p>
    <div class="rule"></div>
    <p class="contact__address">4127 Alder Crest Way<br>Westmoor, CA 91408</p>
    <div class="rule rule--grey"></div>
    <ul class="contact__list">
      <li><svg class="icon" viewBox="0 0 16 16"><path d="M3.5 1 6 3.5 4.6 5.6c.9 2.2 2.6 3.9 4.8 4.8L11.5 9 14 11.5 12.5 14C6.5 14 1 8.5 1 2.5Z"/></svg>(555) 014-2268</li>
      <li><svg class="icon" viewBox="0 0 16 16"><path d="M4 0h8a1 1 0 0 1 1 1v14a1 1 0 0 1-1 1H4a1 1 0 0 1-1-1V1a1 1 0 0 1 1-1Zm1 2v10h6V2Zm3 11a1 1 0 1 0 0 2 1 1 0 0 0 0-2Z"/></svg>(555) 019-4730</li>
      <li><svg class="icon" viewBox="0 0 16 16"><path d="M0 3h16v10H0Zm1.5 1.5v.3L8 9l6.5-4.2v-.3Z"/></svg>hello@harborlinecrest.com</li>
      <li><svg class="icon" viewBox="0 0 16 16"><path d="M8 0a8 8 0 1 0 0 16A8 8 0 0 0 8 0Zm0 1.5c.8.9 1.5 2.3 1.8 4H6.2c.3-1.7 1-3.1 1.8-4Zm-3.3 4H2a6.5 6.5 0 0 1 3.6-3.7 10 10 0 0 0-.9 3.7Zm6.6 0a10 10 0 0 0-.9-3.7A6.5 6.5 0 0 1 14 5.5ZM1.6 7h3v2h-3Zm4.5 0h3.8v2H6.1Zm5.3 0h3v2h-3ZM2 10.5h2.7c.1 1.4.4 2.6.9 3.7A6.5 6.5 0 0 1 2 10.5Zm4.2 0h3.6c-.3 1.7-1 3.1-1.8 4-.8-.9-1.5-2.3-1.8-4Zm5.1 0H14a6.5 6.5 0 0 1-3.6 3.7c.5-1.1.8-2.3.9-3.7Z"/></svg>www.harborlinecrest.com</li>
    </ul>
  </div>

  <div class="brand">
    <span class="brand__dot"></span>
    <span class="brand__name">Harborline Crest</span>
    <span class="brand__tag">Insurance Services</span>
    <span class="brand__lines">Auto | Home | Business | Life</span>
  </div>
</section>

</body>
</html>
```